Im open to ideas.. I was thinking on my business cards aswell as my logo. a place for my name. email. phone number and abn..

ive attched a file with my business logo. which i dont love the colours.. i was think a dark background with charcoal letters so something along those colour schumes but im open to ideas..

Business

BRL Constructions

```html
<!DOCTYPE html>
<html lang="en">
<head>
<meta charset="utf-8">
<title>BRL Constructions – Business Card</title>
<link href="https://fonts.googleapis.com/css2?family=Open+Sans:wght@400;600&family=Roboto+Slab:wght@800&display=swap" rel="stylesheet">
<style>
  :root {
    --page-bg: #d9dadc;
    --card-bg: #323235;
    --ink: #f4f4f2;
    --shadow: rgba(0, 0, 0, 0.28);
  }
  html, body {
    margin: 0;
    padding: 0;
    width: 1200px;
    height: 720px;
    overflow: hidden;
    background: var(--page-bg);
  }
  .canvas {
    position: relative;
    width: 1200px;
    height: 720px;
    display: flex;
    align-items: center;
    justify-content: center;
  }
  .business-card {
    position: relative;
    width: 392px;
    height: 640px;
    background: var(--card-bg);
    box-shadow: 0 10px 28px var(--shadow);
    color: var(--ink);
    font-family: "Open Sans", sans-serif;
  }
  .card-frame {
    position: absolute;
    inset: 16px;
    border: 2px solid var(--ink);
    display: flex;
    flex-direction: column;
    align-items: center;
  }
  .name-plate {
    margin-top: 30px;
    width: 300px;
    height: 66px;
    border: 3px solid var(--ink);
    box-sizing: border-box;
    display: flex;
    align-items: center;
    justify-content: center;
    font-family: "Roboto Slab", serif;
    font-weight: 800;
    font-size: 30px;
    letter-spacing: 1px;
  }
  .contact-list {
    list-style: none;
    margin: 58px 0 0;
    padding: 0;
    display: flex;
    flex-direction: column;
    align-items: center;
    gap: 26px;
  }
  .contact-item {
    display: flex;
    flex-direction: column;
    align-items: center;
    gap: 10px;
    font-size: 19px;
    letter-spacing: 0.3px;
  }
  .contact-icon {
    width: 38px;
    height: 38px;
    border: 2px solid var(--ink);
    border-radius: 50%;
    box-sizing: border-box;
    display: flex;
    align-items: center;
    justify-content: center;
  }
  .contact-icon svg { display: block; }
  .abn-label {
    font-size: 9px;
    font-weight: 600;
    letter-spacing: 0.3px;
  }
  .company-name {
    margin-top: auto;
    margin-bottom: 34px;
    font-size: 24px;
    font-weight: 600;
    letter-spacing: 1px;
    text-transform: uppercase;
  }
</style>
</head>
<body>
<main class="canvas">
  <article class="business-card">
    <div class="card-frame">
      <h1 class="name-plate">Jason&nbsp;SMITH</h1>
      <ul class="contact-list">
        <li class="contact-item">
          <span class="contact-icon">
            <svg width="18" height="18" viewBox="0 0 24 24" aria-hidden="true">
              <path fill="var(--ink)" d="M6.6 10.8a15.2 15.2 0 0 0 6.6 6.6l2.2-2.2a1 1 0 0 1 1-.25 11.4 11.4 0 0 0 3.6.57 1 1 0 0 1 1 1V20a1 1 0 0 1-1 1A17 17 0 0 1 3 4a1 1 0 0 1 1-1h3.5a1 1 0 0 1 1 1c0 1.25.2 2.45.57 3.57a1 1 0 0 1-.25 1z"/>
            </svg>
          </span>
          <span class="contact-text">555 555 555</span>
        </li>
        <li class="contact-item">
          <span class="contact-icon">
            <svg width="18" height="14" viewBox="0 0 18 14" aria-hidden="true">
              <rect x="0.75" y="0.75" width="16.5" height="12.5" fill="none" stroke="var(--ink)" stroke-width="1.5"/>
              <path d="M0.75 0.75 9 8 17.25 0.75" fill="none" stroke="var(--ink)" stroke-width="1.5"/>
            </svg>
          </span>
          <span class="contact-text">youremail@email.com</span>
        </li>
        <li class="contact-item">
          <span class="contact-icon"><span class="abn-label">ABN</span></span>
          <span class="contact-text">Abn Number</span>
        </li>
      </ul>
      <p class="company-name">BRL Constructions</p>
    </div>
  </article>
</main>
</body>
</html>
```